Author needs website header

I want a website header that shows me as an author with a attractive tagline and highlights my new book with a Call to Action to get a Free Chapter

Call

```html
<!DOCTYPE html>
<html lang="en">
<head>
<meta charset="utf-8">
<title>Marisol Okafor — Author Header</title>
<link rel="stylesheet" href="https://fonts.googleapis.com/css2?family=Arimo:wght@700&family=Cinzel:wght@400;600&family=Cormorant+Garamond:wght@500;600&family=Didact+Gothic&display=swap">
<style>
  :root {
    --mist: #f6f9fa;
    --haze: #e3ecec;
    --hill-far: #a9c4b3;
    --hill-mid: #6a9f52;
    --hill-near: #9fc243;
    --hill-low: #c2d767;
    --ink: #111111;
    --white: #ffffff;
    --button-fill: rgba(255, 255, 255, 0.25);
    --cover-top: #ffffff;
    --cover-low: #dfe8f1;
    --spine-light: #f4f6f9;
    --spine-shade: #cfd7e1;
    --title-blue: #6f9cc8;
    --title-deep: #4f7fae;
    --spine-ink: #5c6f86;
    --portrait-hair: #2c2220;
    --portrait-skin: #5a3b2e;
    --portrait-jacket: #b9c6d6;
    --portrait-jacket-low: #d3dbe5;
  }
  * { margin: 0; padding: 0; box-sizing: border-box; }
  html, body { width: 1200px; height: 360px; overflow: hidden; background: var(--white); }

  .site-header { position: relative; width: 1200px; height: 360px; overflow: hidden; }

  .landscape {
    position: absolute;
    inset: 0;
    background: linear-gradient(180deg,
      var(--mist) 0%,
      var(--haze) 30%,
      var(--hill-far) 44%,
      var(--hill-mid) 60%,
      var(--hill-near) 80%,
      var(--hill-low) 100%);
  }
  .landscape::after {
    content: "";
    position: absolute;
    inset: 0;
    background: linear-gradient(90deg, rgba(255,255,255,0.5) 0%, rgba(255,255,255,0.12) 45%, rgba(255,255,255,0) 70%);
  }

  .tagline {
    position: absolute;
    left: 44px;
    top: 58px;
    font-family: "Didact Gothic", "Century Gothic", sans-serif;
    font-weight: 400;
    font-size: 47px;
    letter-spacing: 2px;
    word-spacing: -4px;
    color: var(--ink);
    white-space: nowrap;
  }

  .cta { position: absolute; left: 262px; top: 234px; width: 302px; text-align: center; }
  .cta-button {
    display: block;
    width: 302px;
    height: 62px;
    line-height: 58px;
    border: 2px solid var(--white);
    border-radius: 8px;
    background: var(--button-fill);
    font-family: "Arimo", Arial, sans-serif;
    font-weight: 700;
    font-size: 38px;
    letter-spacing: 1px;
    color: var(--white);
    text-decoration: none;
  }
  .cta-note {
    display: block;
    margin: 6px -60px 0;
    font-family: "Didact Gothic", "Century Gothic", sans-serif;
    font-size: 32px;
    letter-spacing: 1px;
    word-spacing: -3px;
    color: var(--ink);
    white-space: nowrap;
  }

  .book-stack {
    position: absolute;
    left: 703px;
    top: 45px;
    height: 293px;
    display: flex;
    filter: drop-shadow(0 6px 10px rgba(0,0,0,0.22));
  }
  .book-spine {
    width: 30px;
    height: 100%;
    background: linear-gradient(90deg, var(--spine-shade) 0%, var(--spine-light) 35%, var(--spine-light) 70%, var(--spine-shade) 100%);
    display: flex;
    flex-direction: column;
    align-items: center;
    padding: 12px 0 10px;
  }
  .spine-title {
    writing-mode: vertical-rl;
    font-family: "Cinzel", Georgia, serif;
    font-size: 10px;
    letter-spacing: 1px;
    color: var(--spine-ink);
    white-space: nowrap;
  }
  .spine-author {
    writing-mode: vertical-rl;
    margin-top: auto;
    font-family: "Cinzel", Georgia, serif;
    font-size: 6px;
    letter-spacing: 0.5px;
    color: var(--spine-ink);
  }
  .spine-mark {
    width: 8px; height: 8px;
    margin-top: 8px;
    background: var(--spine-ink);
    opacity: 0.6;
  }
  .book-cover {
    position: relative;
    width: 130px;
    height: 100%;
    background: linear-gradient(180deg, var(--cover-top) 0%, #f0f5fa 55%, var(--cover-low) 100%);
    text-align: center;
    padding: 20px 8px 0;
  }
  .cover-kicker {
    display: block;
    font-family: "Cormorant Garamond", Georgia, serif;
    font-weight: 600;
    font-size: 19px;
    color: var(--title-blue);
    line-height: 1;
  }
  .cover-small {
    display: block;
    margin-top: 3px;
    font-family: "Cinzel", Georgia, serif;
    font-size: 10px;
    letter-spacing: 1px;
    color: var(--title-deep);
  }
  .cover-title {
    display: block;
    font-family: "Cormorant Garamond", Georgia, serif;
    font-weight: 500;
    font-size: 36px;
    line-height: 0.95;
    color: var(--title-blue);
  }
  .cover-art {
    width: 84px;
    height: 62px;
    margin: 10px auto 0;
    border-radius: 50%;
    background: radial-gradient(circle at 45% 40%, #ffffff 0%, #eef2f6 45%, #c8d3df 100%);
  }
  .cover-blurb {
    margin-top: 14px;
    font-family: "Cormorant Garamond", Georgia, serif;
    font-size: 7px;
    line-height: 1.2;
    color: var(--spine-ink);
  }
  .cover-author {
    position: absolute;
    left: 0; right: 0;
    bottom: 22px;
    font-family: "Cinzel", Georgia, serif;
    font-weight: 600;
    font-size: 9px;
    letter-spacing: 1.5px;
    color: var(--title-deep);
  }
  .cover-quote {
    position: absolute;
    left: 6px; right: 6px;
    bottom: 6px;
    font-family: "Cormorant Garamond", Georgia, serif;
    font-size: 6px;
    color: var(--spine-ink);
  }

  .author-portrait {
    position: absolute;
    left: 905px;
    top: 0;
    width: 295px;
    height: 360px;
    background:
      radial-gradient(ellipse 70px 95px at 175px 130px, var(--portrait-skin) 0%, var(--portrait-skin) 60%, rgba(90,59,46,0) 100%),
      linear-gradient(180deg, var(--portrait-hair) 0%, var(--portrait-hair) 45%, var(--portrait-jacket) 62%, var(--portrait-jacket-low) 100%);
    -webkit-mask-image: linear-gradient(90deg, rgba(0,0,0,0) 0%, #000 22%);
    mask-image: linear-gradient(90deg, rgba(0,0,0,0) 0%, #000 22%);
  }
</style>
</head>
<body>
  <header class="site-header">
    <div class="landscape" role="img" aria-label="Misty green mountain landscape at sunrise"></div>

    <h1 class="tagline">YOUR TAGLINE GOES HERE</h1>

    <div class="cta">
      <a class="cta-button" href="#free-chapter">CALL NOW!</a>
      <span class="cta-note">to get a Free Chapter</span>
    </div>

    <div class="book-stack" aria-label="Following the Quiet Voice by Marisol Okafor">
      <div class="book-spine">
        <span class="spine-title">FOLLOWING THE QUIET VOICE</span>
        <span class="spine-author">OKAFOR</span>
        <span class="spine-mark"></span>
      </div>
      <div class="book-spine">
        <span class="spine-title">FOLLOWING THE QUIET VOICE</span>
        <span class="spine-author">OKAFOR</span>
        <span class="spine-mark"></span>
      </div>
      <div class="book-spine">
        <span class="spine-title">FOLLOWING THE QUIET VOICE</span>
        <span class="spine-author">OKAFOR</span>
        <span class="spine-mark"></span>
      </div>
      <div class="book-cover">
        <span class="cover-kicker">Following</span>
        <span class="cover-small">THE QUIET</span>
        <span class="cover-title">Voice</span>
        <div class="cover-art" role="img" aria-label="Cover illustration in soft white and pale blue"></div>
        <p class="cover-blurb">A journey toward discovering purpose in the quiet, unexpected places</p>
        <span class="cover-author">MARISOL OKAFOR</span>
        <span class="cover-quote">A warm, honest guide for anyone seeking direction</span>
      </div>
    </div>

    <div class="author-portrait" role="img" aria-label="Portrait of author Marisol Okafor smiling, wearing a pale blue jacket"></div>
  </header>
</body>
</html>
```